TRV Electrical – Fridge Magnet & Letterbox Leaflet

Overview
We are a local electrical contractor based in Gooseberry Hill in the Perth Hills (Western Australia).
We are looking for a designer to create:
1️⃣ A fridge magnet design
2️⃣ A matching letterbox leaflet (A6 or DL)
The goal is to create clean, professional marketing that feels local and trustworthy, not flashy advertising.
The designs must feel like a high-quality local trades business, appealing to homeowners in suburbs such as:
Kalamunda
Gooseberry Hill
Lesmurdie
Walliston
Pickering Brook
Design Style
The design should feel:
✔ Local
✔ Authentic
✔ Professional
✔ Trustworthy
✔ Clean and simple
NOT:
✖ Cheap advertising
✖ Overly flashy
✖ Busy or cluttered
Think premium local tradesman, not mass marketing.
Branding
Use our brand colours inspired by our van:
Primary colours
Navy Blue
White
Accent colour
Yellow / gold highlight
Design should match the look of our work van branding.
Images Provided
We will provide:
✔ Company logo
✔ Photo of our branded van in the Perth Hills
The van photo should be used in the leaflet design to reinforce our local presence.
Fridge Magnet Design
Size suggestion:
90mm x 55mm
Purpose:
Homeowners keep this magnet so they can easily call a trusted electrician.
Must include:
TRV Electrical Contracting
Local Perth Hills Electrician
Based in Gooseberry Hill
Phone number (large and clear)
📞 0472 615 904
Services:
• Fault finding
• Switchboard upgrades
• Lighting & power
• Ceiling fans
• Smoke alarm compliance
Also include:
⭐ 110+ Rovlix Reviews
Website:
www.trvelectrical-example.com.au
Design should be very simple and easy to read from across a kitchen.
Leaflet Design
Size options:
A6 or DL
Purpose:
Letterbox drop marketing in Perth Hills suburbs.
Front Side
Headline:
WE'RE WORKING IN YOUR AREA
Subtext:
Local electrician based in Gooseberry Hill
Include:
✔ Photo of our van
✔ TRV logo
✔ Key services
Services:
• Fault finding
• Switchboard upgrades
• Lighting & power
• Ceiling fans
• Smoke alarm compliance
Call to action:
📞 Call Dorian – 0472 615 904
⭐ 110+ Five-Star Rovlix Reviews
Back Side
Headline:
Your Local Perth Hills Electrician
Servicing:
Kalamunda
Gooseberry Hill
Lesmurdie
Walliston
Pickering Brook
Short message:
Reliable electrical work across the Perth Hills.
Call Dorian
📞 0472 615 904
Website:
www.trvelectrical-example.com.au
EC47286
Target Audience
Homeowners in the Perth Hills aged 35–70.
Many homes are older properties and often need electrical upgrades, repairs and safety work.
Design should appeal to homeowners who value reliability and local service.
Deliverables
Designers must provide:
✔ Print-ready files
✔ Editable source files
✔ High resolution files
For:
Fridge magnet
Leaflet front and back
Final Notes
This design should communicate:
✔ Trusted local electrician
✔ Established business
✔ Professional service
✔ Easy to contact
The goal is to create marketing people will keep, not throw away.

```html
<!DOCTYPE html>
<html lang="en">
<head>
<meta charset="utf-8">
<title>TRV Electrical – Leaflet Front and Back</title>
<link rel="stylesheet" href="https://fonts.googleapis.com/css2?family=Poppins:ital,wght@0,400;0,500;0,600;0,700;1,500;1,600;1,700;1,800&display=swap">
<style>
:root{
  --navy:#0d2457;
  --gold:#c47a1e;
  --white:#ffffff;
  --slate:#8f9bb3;
  --ink:#4d4d4f;
  --stage:#737378;
}
*{margin:0;padding:0;box-sizing:border-box}
html,body{width:1200px;height:928px;overflow:hidden}
body{background:var(--stage);font-family:"Poppins",sans-serif;position:relative}
.leaflet{position:absolute;top:196px;width:400px;height:566px;overflow:hidden;background:var(--white)}
.leaflet--front{left:142px}
.leaflet--back{left:661px;background:var(--navy)}
.shapes{position:absolute;left:0;top:0}
.van-photo{position:absolute;left:0;width:400px;background:linear-gradient(180deg,#9fc3e6 0%,#c4d6e4 28%,#6e7f5c 48%,#26345a 60%,#3b4766 72%,#b08e68 88%,#9a7c5c 100%)}
.abs{position:absolute;white-space:nowrap}
.brand-mark{position:absolute;background:var(--white)}
.brand-name{font-weight:500;line-height:1.1}
.services{list-style:none;position:absolute;left:23px;top:345px;color:var(--white);font-size:11.6px;line-height:14.9px}
.services li{display:flex;align-items:center;gap:6px}
.services svg{flex:none}
.stars{color:var(--gold);letter-spacing:1px}
.phone-icon{display:inline-block;vertical-align:middle}
.licence{text-align:center;font-size:14px}
</style>
</head>
<body>

<section class="leaflet leaflet--front">
  <div class="van-photo" style="top:0;height:266px" role="img" aria-label="Photo of the branded TRV work van parked in the Perth Hills bushland"></div>
  <svg class="shapes" width="400" height="566" viewBox="0 0 400 566">
    <polygon points="0,0 233,0 109,109 0,109" fill="var(--navy)"/>
    <rect x="0" y="266" width="400" height="300" fill="var(--white)"/>
    <polygon points="0,241 317,241 223,339 0,339" fill="var(--navy)"/>
    <rect x="0" y="339" width="300" height="88" fill="var(--gold)"/>
    <polygon points="298,331 400,331 400,435 199,435" fill="var(--navy)"/>
    <rect x="0" y="495" width="400" height="32" fill="var(--navy)"/>
    <polygon points="317,495 400,495 400,527 285,527" fill="var(--slate)"/>
  </svg>

  <div class="brand-mark" style="left:22px;top:24px;width:34px;height:50px"></div>
  <div class="abs brand-name" style="left:67px;top:34px;color:var(--white);font-size:12.5px">TRV Electrical<br>Contracting</div>

  <div class="abs" style="left:27px;top:254px;color:var(--white);font-weight:700;font-size:20.5px;letter-spacing:-.2px">WE'RE WORKING IN</div>
  <div class="abs" style="left:27px;top:281px;color:var(--gold);font-weight:800;font-style:italic;font-size:31px;letter-spacing:-.3px">YOUR AREA</div>

  <ul class="services">
    <li><svg width="8" height="7" viewBox="0 0 8 7"><path d="M1 3.5 3 5.5 7 1" fill="none" stroke="var(--navy)" stroke-width="1.3"/></svg>Fault finding</li>
    <li><svg width="8" height="7" viewBox="0 0 8 7"><path d="M1 3.5 3 5.5 7 1" fill="none" stroke="var(--navy)" stroke-width="1.3"/></svg>Switchboard upgrades</li>
    <li><svg width="8" height="7" viewBox="0 0 8 7"><path d="M1 3.5 3 5.5 7 1" fill="none" stroke="var(--navy)" stroke-width="1.3"/></svg>Lighting &amp; power</li>
    <li><svg width="8" height="7" viewBox="0 0 8 7"><path d="M1 3.5 3 5.5 7 1" fill="none" stroke="var(--navy)" stroke-width="1.3"/></svg>Ceiling fans</li>
    <li><svg width="8" height="7" viewBox="0 0 8 7"><path d="M1 3.5 3 5.5 7 1" fill="none" stroke="var(--navy)" stroke-width="1.3"/></svg>Smoke alarm compliance</li>
  </ul>

  <div class="abs" style="right:24px;top:341px;text-align:right;color:var(--white);font-style:italic;font-weight:500;font-size:16.5px;line-height:20.5px">Local<br>electrician<br>based in<br>Gooseberry Hill</div>

  <div class="abs" style="left:16px;top:451px;color:var(--ink);font-weight:700;font-size:22.5px">Call Dorian</div>
  <div class="abs" style="left:178px;top:446px;color:var(--gold);font-weight:700;font-size:28.5px;display:flex;align-items:center;gap:6px">
    <svg class="phone-icon" width="19" height="19" viewBox="0 0 24 24"><path d="M6.6 10.8a15 15 0 0 0 6.6 6.6l2.2-2.2c.3-.3.7-.4 1-.2 1.1.4 2.3.6 3.6.6.6 0 1 .4 1 1V20c0 .6-.4 1-1 1A17 17 0 0 1 3 4c0-.6.4-1 1-1h3.5c.6 0 1 .4 1 1 0 1.3.2 2.5.6 3.6.1.3 0 .7-.2 1z" fill="var(--navy)"/></svg>0472 615 904</div>

  <div class="abs" style="left:22px;top:502px;color:var(--white);font-size:12.3px;display:flex;gap:9px;align-items:center"><span class="stars">★★★★★</span>110+ Five-Star Rovlix Reviews</div>
  <div class="abs licence" style="left:300px;top:502px;width:100px;color:var(--white)">EC47286</div>

  <div class="abs" style="left:0;top:537px;width:400px;text-align:center;color:var(--navy);font-size:12px;letter-spacing:2.2px">www.trvelectrical-example.com.au</div>
</section>

<section class="leaflet leaflet--back">
  <div class="van-photo" style="top:166px;height:207px" role="img" aria-label="Photo of the branded TRV work van on a Perth Hills lookout"></div>
  <svg class="shapes" width="400" height="566" viewBox="0 0 400 566">
    <polygon points="245,24 400,24 400,188 70,188" fill="var(--gold)"/>
    <polygon points="0,39 328,39 169,166 0,166" fill="var(--white)"/>
    <rect x="0" y="63" width="12" height="76" fill="var(--gold)"/>
    <rect x="0" y="443" width="400" height="37" fill="var(--gold)"/>
    <rect x="0" y="515" width="400" height="33" fill="var(--white)"/>
    <polygon points="316,515 400,515 400,548 285,548" fill="var(--slate)"/>
  </svg>

  <div class="brand-mark" style="left:26px;top:63px;width:55px;height:76px;background:var(--navy)"></div>
  <div class="abs brand-name" style="left:95px;top:78px;color:var(--navy);font-size:21px;line-height:26px">TRV Electrical<br>Contracting</div>

  <div class="abs" style="right:23px;top:49px;text-align:right;color:var(--white);font-weight:700;line-height:29.5px">
    <div style="font-size:19.5px;line-height:26px">Your</div>
    <div style="font-size:25.5px">Local</div>
    <div style="font-size:25.5px">Perth Hills</div>
    <div style="font-size:25.5px">Electrician</div>
  </div>

  <div class="abs" style="left:14px;top:358px;width:373px;height:48px;border-radius:6px;background:var(--gold);display:flex;align-items:center;justify-content:center;gap:10px">
    <span style="color:var(--white);font-weight:700;font-size:18.5px">Call Dorian</span>
    <span style="color:var(--navy);font-weight:700;font-size:28.5px;display:flex;align-items:center;gap:5px">
      <svg class="phone-icon" width="20" height="20" viewBox="0 0 24 24"><path d="M6.6 10.8a15 15 0 0 0 6.6 6.6l2.2-2.2c.3-.3.7-.4 1-.2 1.1.4 2.3.6 3.6.6.6 0 1 .4 1 1V20c0 .6-.4 1-1 1A17 17 0 0 1 3 4c0-.6.4-1 1-1h3.5c.6 0 1 .4 1 1 0 1.3.2 2.5.6 3.6.1.3 0 .7-.2 1z" fill="var(--navy)"/></svg>0472 615 904</span>
  </div>

  <div class="abs" style="left:0;top:413px;width:400px;text-align:center;color:var(--white);font-style:italic;font-weight:500;font-size:14.5px">Reliable electrical work across the Perth Hills.</div>

  <div class="abs" style="left:0;top:450px;width:400px;display:flex;justify-content:center;align-items:center;gap:12px;color:var(--white);font-size:16px"><span class="stars" style="color:var(--navy);font-size:17px">★★★★★</span>110+ Five-Star Rovlix Reviews</div>

  <div class="abs" style="left:0;top:489px;width:400px;text-align:center;color:var(--white);font-size:10.3px;word-spacing:1px">Walliston &nbsp;|&nbsp; Lesmurdie &nbsp;|&nbsp; Kalamunda &nbsp;|&nbsp; Gooseberry Hill &nbsp;|&nbsp; Pickering Brook</div>

  <div class="abs" style="left:22px;top:523px;width:258px;text-align:left;color:var(--navy);font-size:11.2px;letter-spacing:1.1px">www.trvelectrical-example.com.au</div>
  <div class="abs licence" style="left:306px;top:522px;width:94px;color:var(--navy)">EC47286</div>
</section>

</body>
</html>
```